Company Holiday Card

Please design a corporate holiday card for our investment firm. Our firm invests in Media & Entertainment assets so incorporating some of that imagery in a creative and festive way would be ideal so that the card doesn't feel so generic.

I have attached some design inspiration that could be cute if we're able to incorporate Media & Entertainment images into those scenes. Things like a film roll, movie cut board, video game console, music notes, sports balls (soccer, football, etc.), event tickets, microphone, kalder, etc. I have also attached two versions of our logo in case that's helpful.

The audience will be private equity investors and counterparties so we would still like to keep it polished and professional.

```html
<!DOCTYPE html>
<html lang="en">
<head>
<meta charset="utf-8">
<title>Holiday Card – Northfield Capital</title>
<link rel="stylesheet" href="https://fonts.googleapis.com/css2?family=Yellowtail&family=Dancing+Script:wght@700&family=Montserrat:wght@400&family=Barlow:wght@500&display=block">
<style>
  :root {
    --page: #ffffff;
    --navy: #1c2a57;
    --white: #ffffff;
    --wreath-green: #2f7d74;
    --wreath-red: #b83a3a;
    --wreath-gold: #d9a441;
    --logo-blue: #ffffff;
  }
  html, body {
    margin: 0;
    padding: 0;
    width: 1032px;
    height: 1200px;
    overflow: hidden;
    background: var(--page);
  }
  .card {
    position: absolute;
    left: 79px;
    top: 8px;
    width: 874px;
    height: 1184px;
    background: var(--navy);
    color: var(--white);
  }
  .wreath {
    position: absolute;
    left: 61px;
    top: 127px;
    width: 740px;
    height: 740px;
  }
  .greeting {
    position: absolute;
    left: 0;
    width: 100%;
    top: 330px;
    margin: 0;
    text-align: center;
    font-family: "Yellowtail", "Dancing Script", "Brush Script MT", cursive;
    font-weight: 400;
    line-height: 1;
  }
  .greeting__line {
    display: block;
    font-size: 124px;
    transform: rotate(-4deg);
  }
  .greeting__line--first { margin-left: 70px; }
  .greeting__line--second { margin-top: 0; margin-right: 10px; }
  .sign-off {
    position: absolute;
    left: 0;
    width: 100%;
    top: 968px;
    margin: 0;
    text-align: center;
    font-family: "Montserrat", sans-serif;
    font-size: 16px;
    letter-spacing: 4px;
    text-transform: uppercase;
  }
  .company {
    position: absolute;
    left: 0;
    width: 100%;
    top: 1036px;
    display: flex;
    justify-content: center;
    align-items: center;
    gap: 16px;
    font-family: "Barlow", sans-serif;
    font-weight: 500;
    font-size: 50px;
    letter-spacing: 0.5px;
    line-height: 1;
    color: var(--logo-blue);
    text-transform: uppercase;
  }
  .company__mark {
    width: 22px;
    height: 22px;
    background: var(--logo-blue);
  }
</style>
</head>
<body>
  <main class="card">
    <svg class="wreath" viewBox="0 0 740 740" role="img"
         aria-label="Festive wreath illustration of holly, gifts, candy canes, film clapperboards, film reel, microphone, kalder, music notes and soccer ball">
      <defs>
        <linearGradient id="wreathTone" x1="0" y1="0" x2="1" y2="1">
          <stop offset="0" stop-color="var(--wreath-green)"/>
          <stop offset="0.5" stop-color="var(--wreath-gold)"/>
          <stop offset="1" stop-color="var(--wreath-red)"/>
        </linearGradient>
      </defs>
      <circle cx="370" cy="370" r="318" fill="none" stroke="url(#wreathTone)" stroke-width="84" opacity="0.45"/>
    </svg>

    <h1 class="greeting">
      <span class="greeting__line greeting__line--first">Merry</span>
      <span class="greeting__line greeting__line--second">Christmas</span>
    </h1>

    <p class="sign-off">Season’s greetings from</p>

    <div class="company">
      <span class="company__mark"></span>
      <span class="company__name">Northfield Capital</span>
    </div>
  </main>
</body>
</html>
```